Telecommunications/Power civil contractor needs business card design

Were a new telecommunications/power underground civil contractor that is looking for a new business card design. Our company colours are silver or grey and orange. Feel free to use the white background logo or the black background logo.

Target Market(s)

Local contractors, utility companies, private sector mining/energy companies, developers.

Industry/Entity Type

Telecommunications

Contact Information for Business Card

Each card will need the following info:
Persons name:
Title:
E-mail:
Phone number:
Shop Address:
Mailing Address:

Requirements
Must have
• Each card will need the following info:
• Persons name:
• Title:
• E-mail:
• Phone number:
• Shop Address:
• Mailing Address:

```html
<!DOCTYPE html>
<html lang="en">
<head>
<meta charset="utf-8">
<title>Ridgeline Contracting Inc – Business Card</title>
<link href="https://fonts.googleapis.com/css2?family=Open+Sans:wght@400;600;700&display=swap" rel="stylesheet">
<style>
  :root {
    --orange: #f15a22;
    --orange-light: #f7864f;
    --grey: #8a8a8a;
    --grey-dark: #4a4c4f;
    --grey-darker: #2f3133;
    --text: #3d3d3d;
    --white: #ffffff;
    --paper: #f4f4f4;
    --backdrop: #d9dadb;
  }
  * { box-sizing: border-box; margin: 0; padding: 0; }
  html, body {
    width: 1200px; height: 950px; overflow: hidden;
    background: var(--backdrop);
    font-family: "Open Sans", Arial, sans-serif;
  }
  .sheet {
    width: 1200px; height: 950px;
    display: flex; flex-direction: column; align-items: center; justify-content: center;
    gap: 50px;
  }
  .card {
    position: relative;
    width: 700px; height: 400px;
    overflow: hidden;
    box-shadow: 0 6px 18px rgba(0,0,0,.18);
  }
  /* Back side */
  .card-back {
    background: linear-gradient(160deg, var(--grey-dark), var(--grey-darker));
    display: flex; align-items: center; justify-content: center; gap: 22px;
  }
  .card-back .brand-mark {
    width: 110px; height: 110px; border-radius: 50%;
    border: 7px solid #c9cacb;
  }
  .card-back .brand-name {
    color: #c9cacb; font-weight: 700; font-size: 30px; line-height: 1.15;
    text-transform: uppercase; letter-spacing: 1px;
  }
  /* Front side */
  .card-front { background: var(--paper); }
  .card-front .wave { position: absolute; inset: 0; }
  .person {
    position: absolute; right: 44px; top: 92px; text-align: right; color: var(--white);
  }
  .person-name { font-weight: 700; font-size: 24px; }
  .person-title { font-size: 19px; }
  .contact {
    position: absolute; left: 40px; top: 196px;
    color: var(--text); font-size: 18px; line-height: 1.3;
    list-style: none;
  }
  .contact .address { margin-bottom: 8px; }
  .contact li { display: flex; align-items: center; gap: 10px; }
  .contact svg { width: 16px; height: 16px; flex: none; }
  .contact .no-icon { padding-left: 26px; }
  .brand {
    position: absolute; right: 40px; bottom: 50px;
    display: flex; align-items: center; gap: 14px;
  }
  .brand-mark-front {
    width: 70px; height: 70px; border-radius: 50%;
    border: 5px solid var(--orange);
  }
  .brand-name-front {
    color: var(--orange); font-weight: 700; font-size: 26px; line-height: 1.1;
    text-transform: uppercase; letter-spacing: 1px;
  }
</style>
</head>
<body>
<main class="sheet">
  <section class="card card-back" aria-label="Card back">
    <span class="brand-mark"></span>
    <span class="brand-name">Ridgeline<br>Contracting Inc</span>
  </section>

  <section class="card card-front" aria-label="Card front">
    <svg class="wave" viewBox="0 0 700 400" preserveAspectRatio="none" aria-hidden="true">
      <defs>
        <linearGradient id="bandFill" x1="0" x2="1" y1="0" y2="0">
          <stop offset="0" stop-color="var(--orange)"/>
          <stop offset="0.6" stop-color="var(--orange-light)"/>
          <stop offset="1" stop-color="var(--orange)"/>
        </linearGradient>
      </defs>
      <path d="M0,0 H700 V205 C590,212 470,170 330,105 C220,55 100,55 0,95 Z" fill="url(#bandFill)"/>
      <path d="M0,105 C110,62 220,62 330,112 C470,180 590,222 700,216 V228 C585,234 465,192 325,124 C215,72 105,74 0,118 Z" fill="var(--grey)"/>
      <path d="M60,96 C150,58 240,62 300,88" stroke="var(--white)" stroke-width="3" fill="none"/>
    </svg>

    <div class="person">
      <div class="person-name">Sam Keller</div>
      <div class="person-title">President</div>
    </div>

    <ul class="contact">
      <li class="address no-icon" style="padding-left:0;display:block">1420 Alder Lane<br>Brookvale, NY 11500</li>
      <li>
        <svg viewBox="0 0 16 16"><circle cx="8" cy="8" r="8" fill="var(--orange)"/><path d="M5 4.5c0 4 2.5 7 6.5 7l.5-1.8-2-1-1 1c-1.2-.6-2-1.5-2.6-2.7l1-1-1-2z" fill="var(--white)"/></svg>
        555 0142 7788
      </li>
      <li>
        <svg viewBox="0 0 16 16"><rect x="1" y="3" width="14" height="10" rx="1" fill="var(--orange)"/><path d="M1.5 3.5 8 8.5l6.5-5" stroke="var(--white)" stroke-width="1.3" fill="none"/></svg>
        sam@ridgeline.example
      </li>
      <li>
        <svg viewBox="0 0 16 16"><circle cx="8" cy="8" r="8" fill="var(--orange)"/><circle cx="8" cy="8" r="4" fill="none" stroke="var(--white)" stroke-width="1.3"/><path d="M4 8h8" stroke="var(--white)" stroke-width="1.3"/></svg>
        www.ridgeline.example
      </li>
    </ul>

    <div class="brand">
      <span class="brand-mark-front"></span>
      <span class="brand-name-front">Ridgeline<br>Contracting Inc</span>
    </div>
  </section>
</main>
</body>
</html>
```